Business Card Design

We need a business card design for a new dental practice in Brisbane. I'd like the basic details and logo on one side and appointment schedule on the other side. It is based in CBD office area and would prefer a professional and modern design.
Target Market(s)
20-60 years old office workers and residents with high education levels
Industry/Entity Type
Dental
Contact Information for Business Card
Harbourlight Dental
Dr Marcus Lindqvist
Principal Dentist
07 3194 6627
admin@harbourlightdentistry.example.au
www.harbourlightdentistry.example.au
S27, Level 3, Ferndale North Tower, 318 Gorrick St, Alderwood Heights, QLD 4118

```html
<!DOCTYPE html>
<html lang="en">
<head>
<meta charset="utf-8">
<title>Harbourlight Dental – Business Card</title>
<link rel="stylesheet" href="https://fonts.googleapis.com/css2?family=Questrial&display=swap">
<style>
  :root {
    --backdrop: #d6d7d8;
    --brand-blue: #1457a8;
    --soft-blue: #4aa6de;
    --ink: #1d2431;
    --paper: #ffffff;
    --paper-faint: rgba(255,255,255,0.55);
    --card-w: 520px;
    --card-h: 297px;
  }
  * { box-sizing: border-box; margin: 0; padding: 0; }
  html, body { width: 1200px; height: 900px; overflow: hidden; }
  body {
    background: var(--backdrop);
    font-family: "Questrial", "Century Gothic", sans-serif;
    display: flex;
    align-items: center;
    justify-content: center;
    gap: 60px;
  }
  .card {
    position: relative;
    width: var(--card-w);
    height: var(--card-h);
    overflow: hidden;
    box-shadow: 0 6px 18px rgba(0,0,0,0.18);
  }
  .tab { position: absolute; height: 20px; }

  /* Front */
  .card-front { background: var(--paper); }
  .card-front .tab { background: var(--brand-blue); }
  .card-front .tab-top { top: 0; left: 0; width: 58%; border-radius: 0 0 8px 0; }
  .card-front .tab-bottom { bottom: 0; right: 0; width: 62%; border-radius: 8px 0 0 0; }
  .brand {
    position: absolute;
    top: 112px;
    left: 0; right: 0;
    display: flex;
    align-items: center;
    justify-content: center;
    gap: 12px;
  }
  .brand-dot {
    width: 34px; height: 34px;
    border-radius: 50%;
    background: var(--soft-blue);
  }
  .brand-name {
    font-size: 38px;
    color: var(--ink);
    letter-spacing: -0.5px;
  }
  .front-url {
    position: absolute;
    top: 192px;
    right: 58px;
    font-size: 13px;
    color: var(--brand-blue);
    letter-spacing: 0.2px;
  }

  /* Back */
  .card-back { background: var(--brand-blue); color: var(--paper); }
  .card-back .tab { background: var(--paper); }
  .card-back .tab-top { top: 0; right: 0; width: 46%; border-radius: 0 0 0 8px; }
  .card-back .tab-bottom { bottom: 0; left: 0; width: 42%; border-radius: 0 8px 0 0; }
  .contact-name {
    position: absolute;
    top: 42px;
    left: 36px;
    right: 24px;
    font-size: 13px;
    letter-spacing: 0.6px;
    text-transform: uppercase;
    white-space: nowrap;
  }
  .contact-name .divider { margin: 0 6px; }
  .contact {
    position: absolute;
    top: 76px;
    left: 36px;
    width: 270px;
  }
  .contact-list { list-style: none; }
  .contact-list li {
    display: flex;
    align-items: flex-start;
    gap: 10px;
    font-size: 11.5px;
    line-height: 1.45;
    margin-bottom: 8px;
    white-space: nowrap;
  }
  .contact-icon {
    flex: 0 0 14px;
    width: 14px; height: 14px;
    margin-top: 1px;
  }
  .schedule {
    position: absolute;
    top: 76px;
    left: 322px;
    width: 174px;
  }
  .schedule-title {
    font-size: 11.5px;
    letter-spacing: 0.6px;
    text-transform: uppercase;
    padding-bottom: 6px;
    border-bottom: 1px solid var(--paper);
  }
  .schedule-table {
    width: 100%;
    border-collapse: collapse;
    font-size: 10.5px;
  }
  .schedule-table th {
    font-weight: 400;
    text-align: left;
    color: var(--paper-faint);
    padding: 6px 0 2px;
  }
  .schedule-table td {
    height: 26px;
    border-bottom: 1px solid var(--paper-faint);
  }
</style>
</head>
<body>
  <section class="card card-front" aria-label="Business card front">
    <div class="tab tab-top"></div>
    <div class="brand">
      <span class="brand-dot" aria-hidden="true"></span>
      <span class="brand-name">Harbourlight Dental</span>
    </div>
    <p class="front-url">www.harbourlightdentistry.example.au</p>
    <div class="tab tab-bottom"></div>
  </section>

  <section class="card card-back" aria-label="Business card back">
    <div class="tab tab-top"></div>
    <p class="contact-name">Dr Marcus Lindqvist<span class="divider">|</span>Principal Dentist</p>
    <div class="contact">
      <ul class="contact-list">
        <li>
          <svg class="contact-icon" viewBox="0 0 14 14" aria-hidden="true">
            <circle cx="7" cy="7" r="7" fill="#fff"/>
            <path d="M7 3.2a2.4 2.4 0 0 0-2.4 2.4C4.6 7.4 7 10.6 7 10.6s2.4-3.2 2.4-5A2.4 2.4 0 0 0 7 3.2z" fill="#1457a8"/>
            <circle cx="7" cy="5.6" r="0.9" fill="#fff"/>
          </svg>
          <span>S27, Level 3, Ferndale North Tower,<br>318 Gorrick St, Alderwood Heights,<br>QLD 4118</span>
        </li>
        <li>
          <svg class="contact-icon" viewBox="0 0 14 14" aria-hidden="true">
            <circle cx="7" cy="7" r="7" fill="#fff"/>
            <path d="M4.6 3.6l1.3-.3.8 1.8-.9.7a5 5 0 0 0 2.4 2.4l.7-.9 1.8.8-.3 1.3c-3.2.3-6.1-2.6-5.8-5.8z" fill="#1457a8"/>
          </svg>
          <span>07 3194 6627</span>
        </li>
        <li>
          <svg class="contact-icon" viewBox="0 0 14 14" aria-hidden="true">
            <circle cx="7" cy="7" r="7" fill="#fff"/>
            <circle cx="7" cy="7" r="3.6" fill="none" stroke="#1457a8" stroke-width="0.9"/>
            <ellipse cx="7" cy="7" rx="1.5" ry="3.6" fill="none" stroke="#1457a8" stroke-width="0.8"/>
            <line x1="3.4" y1="7" x2="10.6" y2="7" stroke="#1457a8" stroke-width="0.8"/>
          </svg>
          <span>www.harbourlightdentistry.example.au</span>
        </li>
        <li>
          <svg class="contact-icon" viewBox="0 0 14 14" aria-hidden="true">
            <circle cx="7" cy="7" r="7" fill="#fff"/>
            <rect x="3.5" y="4.5" width="7" height="5" fill="none" stroke="#1457a8" stroke-width="0.9"/>
            <path d="M3.5 4.5L7 7.3l3.5-2.8" fill="none" stroke="#1457a8" stroke-width="0.9"/>
          </svg>
          <span>admin@harbourlightdentistry.example.au</span>
        </li>
      </ul>
    </div>
    <div class="schedule">
      <p class="schedule-title">Your Appointments</p>
      <table class="schedule-table">
        <thead>
          <tr><th>Date</th><th>Time</th></tr>
        </thead>
        <tbody>
          <tr><td></td><td></td></tr>
          <tr><td></td><td></td></tr>
          <tr><td></td><td></td></tr>
        </tbody>
      </table>
    </div>
    <div class="tab tab-bottom"></div>
  </section>
</body>
</html>
```